BLIP! Card

The single side "business card" will be utilized to write down product information for our customers. The card needs to include our logo in josefin font and read BLIP! on the front. Our brand colors are espresso brown and copper. The back needs to be white (blank) to allow us to write information down. We want modern, bold, clean and fun.
I have attached a copy of our logo but you do not have to utilize exactly as shown.

Industry/Entity Type

Business

```html
<!DOCTYPE html>
<html lang="en">
<head>
<meta charset="utf-8">
<title>harlows — blip! card</title>
<link rel="stylesheet" href="https://fonts.googleapis.com/css2?family=Josefin+Sans:wght@300;400&display=swap">
<style>
  :root {
    --espresso: #2b1a12;
    --copper: #c96a27;
    --backdrop: #e9e8ea;
  }
  * { margin: 0; padding: 0; box-sizing: border-box; }
  html, body {
    width: 1200px;
    height: 900px;
    overflow: hidden;
    background: var(--backdrop);
  }
  .stage {
    width: 1200px;
    height: 900px;
    display: flex;
    align-items: center;
    justify-content: center;
  }
  .card {
    position: relative;
    width: 440px;
    height: 770px;
    background: var(--espresso);
    font-family: "Josefin Sans", sans-serif;
    color: var(--copper);
  }
  .brand {
    position: absolute;
    left: 58px;
    top: 318px;
  }
  .brand-name {
    font-weight: 300;
    font-size: 78px;
    line-height: 1;
    letter-spacing: 3px;
  }
  .brand-tagline {
    font-weight: 300;
    font-size: 27px;
    line-height: 1;
    margin-top: 18px;
    margin-left: 4px;
    letter-spacing: 0.5px;
  }
  .accent-band {
    position: absolute;
    left: 0;
    right: 0;
    top: 670px;
    height: 56px;
  }
  .accent-band rect { fill: var(--copper); }
  .callout {
    position: absolute;
    right: 12px;
    top: 680px;
    font-weight: 400;
    font-size: 44px;
    line-height: 1;
    color: var(--espresso);
    letter-spacing: 2px;
  }
</style>
</head>
<body>
  <main class="stage">
    <article class="card">
      <div class="brand">
        <h1 class="brand-name">harlows</h1>
        <p class="brand-tagline">Jewelry &amp; Design Studio</p>
      </div>
      <svg class="accent-band" viewBox="0 0 440 56" preserveAspectRatio="none" aria-hidden="true">
        <rect x="0" y="0" width="440" height="56"/>
      </svg>
      <p class="callout">blip!</p>
    </article>
  </main>
</body>
</html>
```